Quarry Ledger Systems Design

I would like a construction focused flyer design (if possible, inline with the current design esthetic from my website www.rovelquip.com), 1 standard US page (8.5x11"), front and back, full color glossy. I want a design I can use for multiple software partners, so I want the ability to edit the template that is created. This can be full page or folded- whatever you think is best.Attached are my logos, and a current flyer. I want to use the logo and the color scheme- feel free to make the logo colors even brighter. Everything else can be changed! Any additional graphics should be software or construction focused.

Target Market(s)

Electrical, Mechanical and Plumbing Construction Companies, specifically their accounting, IT, purchasing staff.

Font styles to use
Sans Serif

Colors
6b449b
9ccb3b

Requirements
Must have
• Lots of construction oriented graphics. Discreet boxes for text that can be changed in using photoshop or Illustrator products CS6 or earlier.
• Designs should be:
• - B2B focused
• - merge technology and construction
• - Show how technology can save time
• - Automation is a good thing
Should not have
• Be saved in a format that can not be used by CS6 or earlier.

```html
<!DOCTYPE html>
<html lang="en">
<head>
<meta charset="utf-8">
<title>Quarry Ledger Systems – Flyer</title>
<link href="https://fonts.googleapis.com/css2?family=Abel&family=Montserrat:wght@800&family=Open+Sans:wght@400;600&display=swap" rel="stylesheet">
<style>
:root{
  --purple:#6b449b;
  --green:#58b947;
  --green-text:#3d9a33;
  --green-bright:#9ccb3b;
  --ink:#333;
  --paper:#fff;
  --stage:#3b3b3d;
}
*{box-sizing:border-box;margin:0;padding:0}
html,body{width:1200px;height:776px;overflow:hidden;background:var(--stage)}
body{display:flex;gap:30px;padding:28px;font-family:"Open Sans",sans-serif;color:var(--ink)}
.page{position:relative;width:557px;height:720px;background:var(--paper);overflow:hidden;flex:none}

/* front */
.hero-photo{position:absolute;left:0;top:0;width:557px;height:230px;background:linear-gradient(120deg,#3c3552 0%,#5a4a6e 45%,#3a3246 100%)}
.hero-title-box{position:absolute;left:0;top:0;width:275px;height:230px;background:rgba(26,120,60,.85)}
.hero-title{position:absolute;left:38px;top:44px;font-family:"Montserrat",sans-serif;font-weight:800;color:#fff;line-height:1.02;font-size:34px;letter-spacing:.5px}
.hero-title span{display:block}
.hero-chevron{position:absolute;left:20px;top:145px}
.tagline-band{position:absolute;left:0;top:230px;width:557px;height:38px;background:var(--purple);color:#fff;font-size:12.5px;font-weight:600;display:flex;align-items:center;justify-content:center}
.productivity{position:absolute;left:0;top:276px;width:557px;text-align:center}
.productivity h2{font-family:"Abel",sans-serif;font-weight:400;color:var(--purple);font-size:24px;letter-spacing:.3px;line-height:1.2}
.productivity .rule{width:420px;height:2px;background:var(--purple);margin:2px auto 3px}
.productivity p{font-family:"Abel",sans-serif;color:var(--purple);font-size:15px;line-height:1.2}
.feature{position:absolute;width:250px;text-align:center;font-family:"Abel",sans-serif}
.feature .icon{width:60px;height:60px;border-radius:50%;background:var(--purple);margin:0 auto 6px;display:flex;align-items:center;justify-content:center}
.feature h3{font-weight:400;font-size:14px;line-height:1.2;color:var(--green)}
.feature p{font-size:14px;line-height:1.2;color:var(--green-text)}
.about{position:absolute;left:0;top:562px;width:557px;height:158px;background:var(--green);color:#fff;text-align:center;padding-top:20px}
.about h2{font-family:"Abel",sans-serif;font-weight:400;font-size:22px}
.about .rule{width:400px;height:2px;background:#fff;margin:6px auto 10px}
.about p{font-size:10.5px;line-height:1.5;padding:0 50px}

/* back */
.products-intro{position:absolute;left:40px;top:48px;width:300px}
.products-intro h2{font-family:"Abel",sans-serif;font-weight:400;color:var(--purple);font-size:24px;margin-bottom:4px}
.products-intro p{font-size:9px;line-height:1.45}
.device-mock{position:absolute;left:345px;top:22px;width:180px;height:135px;border-radius:6px;background:linear-gradient(160deg,#2b2b2b,#55595f 60%,#9aa3a8)}
.product{position:absolute;width:225px}
.product h3{font-family:"Abel",sans-serif;font-weight:400;font-size:16px;line-height:1.3;color:#222;display:flex;align-items:center;gap:8px;margin-bottom:3px}
.product p{font-size:8.5px;line-height:1.45;padding-left:6px}
.product-band{position:absolute;left:0;top:330px;width:557px;height:245px;background:var(--purple);color:#fff}
.suite{position:absolute;top:16px;width:170px}
.suite .ring{width:66px;height:66px;border:3px solid #fff;border-radius:50%;margin:0 auto 10px;display:flex;align-items:center;justify-content:center}
.suite h3{font-family:"Abel",sans-serif;font-weight:400;font-size:14px;line-height:1.2;text-align:center;margin-bottom:6px}
.suite ul{font-family:"Abel",sans-serif;font-size:10.5px;line-height:1.35;padding-left:14px}
.contact{position:absolute;left:0;top:575px;width:557px;height:125px}
.brand{position:absolute;left:30px;top:22px;display:flex;align-items:center;gap:10px}
.brand .mark{width:22px;height:22px;background:var(--purple)}
.brand .name{font-family:"Abel",sans-serif;font-size:13px;color:var(--purple);width:80px;line-height:1.15}
.contact-lines{position:absolute;left:140px;top:14px;font-family:"Abel",sans-serif;color:#333}
.contact-lines .phone{font-size:24px;line-height:1.2}
.contact-lines p{font-size:15px;line-height:1.3}
.social-panel{position:absolute;right:0;top:0}
.green-foot{position:absolute;left:0;top:700px;width:557px;height:20px;background:var(--green)}
</style>
</head>
<body>

<section class="page front">
  <div class="hero-photo" role="img" aria-label="Photo of a team meeting in a modern open office, tinted purple"></div>
  <div class="hero-title-box"></div>
  <h1 class="hero-title"><span>QUARRY</span><span>LEDGER</span><span>SYSTEMS</span></h1>
  <svg class="hero-chevron" width="290" height="80" viewBox="0 0 290 80">
    <polyline points="0,70 140,18 285,50" fill="none" stroke="#fff" stroke-width="4"/>
  </svg>
  <div class="tagline-band">REJOICE! Purchase Order Creation and Vendor Automation PLUS Invoice Matching!</div>

  <div class="productivity">
    <h2>TAKING PRODUCTIVITY TO THE NEXT LEVEL</h2>
    <div class="rule"></div>
    <p>Swift Purchase - Swift Order - Swift Invoice</p>
  </div>

  <div class="feature" style="left:30px;top:345px">
    <div class="icon">
      <svg width="32" height="28" viewBox="0 0 34 30"><rect x="4" y="4" width="20" height="14" rx="2" fill="#fff"/><path d="M24 7h4a3 3 0 0 1 0 6h-4" fill="none" stroke="#fff" stroke-width="3"/><rect x="1" y="22" width="30" height="4" rx="2" fill="#fff"/></svg>
    </div>
    <h3>IT'S EASY</h3>
    <p>Easily write terrific looking PO's</p>
  </div>
  <div class="feature" style="left:285px;top:335px">
    <div class="icon">
      <svg width="30" height="28" viewBox="0 0 34 30"><polygon points="2,14 32,2 22,28 16,18" fill="#fff"/></svg>
    </div>
    <h3>IT'S A SNAP</h3>
    <p>Create material quote requests in a snap</p>
  </div>
  <div class="feature" style="left:30px;top:455px">
    <div class="icon"><span style="color:#fff;font-size:32px;font-family:'Open Sans',sans-serif;font-weight:600">$</span></div>
    <h3>E-COMMERCE</h3>
    <p>Use the power of automation and data</p>
  </div>
  <div class="feature" style="left:285px;top:445px">
    <div class="icon">
      <svg width="28" height="28" viewBox="0 0 30 30"><rect x="2" y="13" width="6" height="14" fill="#fff"/><path d="M10 13l6-10c3 0 3 3 2 6h8a2 2 0 0 1 2 2l-3 14a2 2 0 0 1-2 2H10z" fill="#fff"/></svg>
    </div>
    <h3>NEVER WASTE TIME</h3>
    <p>Automated matching of PO to Invoice</p>
  </div>

  <div class="about">
    <h2>ABOUT US</h2>
    <div class="rule"></div>
    <p>Quarry Ledger Systems makes the electronic exchange of purchase information seamless, accurate, and cost effective for clients and vendors while providing growth opportunities for our employees.</p>
  </div>
</section>

<section class="page back">
  <div class="products-intro">
    <h2>OUR PRODUCTS</h2>
    <p>With over 25 years in the construction industry, we understand the frustration of inefficient procurement processes, the financial pains and ramifications of setbacks, and the need for consistently flawless execution of purchasing tasks. With an industry average of less than 6% profit per project, we know what's on the line.</p>
  </div>
  <div class="device-mock" role="img" aria-label="Desktop, tablet and phone screens showing the software website"></div>

  <div class="product" style="left:40px;top:178px">
    <h3><span style="color:var(--purple);font-size:18px;font-family:'Open Sans',sans-serif;font-weight:600;line-height:1">$</span>SWIFT PURCHASE</h3>
    <p>Swift Purchase is a comprehensive, easy-to-use software package for material management.</p>
  </div>
  <div class="product" style="left:300px;top:170px">
    <h3><svg width="18" height="16" viewBox="0 0 34 30"><polygon points="2,14 32,2 22,28 16,18" fill="#6b449b"/></svg>SWIFT INVOICE</h3>
    <p>Tired of trying to match invoice items to order items? Swift Invoice builds on what Swift Order Confirmation started.</p>
  </div>
  <div class="product" style="left:40px;top:244px">
    <h3><svg width="22" height="14" viewBox="0 0 22 14"><path d="M2 13a9 9 0 0 1 18 0" fill="none" stroke="#6b449b" stroke-width="3"/><line x1="11" y1="13" x2="15" y2="6" stroke="#6b449b" stroke-width="2"/></svg>SWIFT ORDER</h3>
    <p>Swift Order Confirmation uses the latest technology to harness all of the information your vendor has about your order and then makes that information available to you.</p>
  </div>
  <div class="product" style="left:300px;top:244px">
    <h3><svg width="18" height="18" viewBox="0 0 18 18"><path d="M2 16l8-8" stroke="#6b449b" stroke-width="4"/><circle cx="12.5" cy="5.5" r="4.5" fill="none" stroke="#6b449b" stroke-width="3"/></svg>SITE TOOL LOG</h3>
    <p>Site Tool Log follows the Swift Purchase design, which incorporates ease of use with an intuitive, user friendly interface.</p>
  </div>

  <div class="product-band">
    <div class="suite" style="left:25px">
      <div class="ring"><svg width="34" height="30" viewBox="0 0 40 36"><rect x="2" y="2" width="36" height="8" fill="#fff"/><rect x="2" y="14" width="36" height="8" fill="#fff"/><rect x="2" y="26" width="36" height="8" fill="#fff"/></svg></div>
      <h3>SWIFT PURCHASE</h3>
      <ul><li>Swiftly create professional-looking POs</li><li>Track orders to jobsites</li><li>Review cumulated jobsite material usage</li><li>Link to your accounting system</li></ul>
    </div>
    <div class="suite" style="left:200px;width:175px">
      <div class="ring"><svg width="36" height="30" viewBox="0 0 42 34"><circle cx="21" cy="9" r="7" fill="#fff"/><circle cx="8" cy="13" r="5" fill="#fff"/><circle cx="34" cy="13" r="5" fill="#fff"/><path d="M9 34a12 12 0 0 1 24 0z" fill="#fff"/><path d="M0 32a8 8 0 0 1 12-7l-3 7z" fill="#fff"/><path d="M42 32a8 8 0 0 0-12-7l3 7z" fill="#fff"/></svg></div>
      <h3>SWIFT ORDER CONFIRMATION</h3>
      <ul><li>Create POs of any size in less than a minute</li><li>Quickly get material orders to your vendors</li><li>No new software is needed for your vendors</li><li>Spend more time managing important materials</li></ul>
    </div>
    <div class="suite" style="left:380px">
      <div class="ring"><svg width="28" height="32" viewBox="0 0 34 38"><ellipse cx="17" cy="6" rx="15" ry="5" fill="#fff"/><path d="M2 10c0 6 30 6 30 0v6c0 6-30 6-30 0z" fill="#fff"/><path d="M2 20c0 6 30 6 30 0v6c0 6-30 6-30 0z" fill="#fff"/><path d="M2 30c0 6 30 6 30 0v2c0 6-30 6-30 0z" fill="#fff"/></svg></div>
      <h3>SWIFT INVOICE</h3>
      <ul><li>Receive your invoices and invoice images daily</li><li>Automatically matches invoice lines to PO lines</li><li>Imports invoice images into your imaging system</li><li>Integrates with your accounting system</li></ul>
    </div>
  </div>

  <div class="contact">
    <svg class="social-panel" width="180" height="80" viewBox="0 0 180 80">
      <polygon points="30,0 180,0 180,80 0,80" fill="#58b947"/>
      <circle cx="66" cy="42" r="16" fill="none" stroke="#fff" stroke-width="2.5"/>
      <circle cx="104" cy="42" r="16" fill="none" stroke="#fff" stroke-width="2.5"/>
      <circle cx="142" cy="42" r="16" fill="none" stroke="#fff" stroke-width="2.5"/>
    </svg>
    <div class="brand"><span class="mark"></span><span class="name">QUARRY LEDGER SYSTEMS</span></div>
    <div class="contact-lines">
      <div class="phone">Phone (800) 555-0142</div>
      <p>Quarry Ledger Systems, Inc.</p>
      <p>PO Box 4821, Dayton, OH 45401</p>
    </div>
  </div>
  <div class="green-foot"></div>
</section>

</body>
</html>
```